Bref créative
R.T. M&P Stationary
Simple
Odel Krasniak
7281 Porravel Blvd.
Suite 382
Ashgrove Heights, CA 90417
odel@tinmarrowseek.com
www.tinmarrowseek.com

```html
<!DOCTYPE html>
<html lang="en">
<head>
<meta charset="utf-8">
<title>R.T. M&amp;P Stationary – Business Card</title>
<link rel="stylesheet" href="https://fonts.googleapis.com/css2?family=Montserrat:wght@400;600&family=Cormorant+SC:wght@500&display=swap">
<style>
  :root {
    --page: #ecebe8;
    --card-edge: #f4df9c;
    --card-gold: #cda547;
    --ink-light: #fbefc6;
    --ink-soft: #f3e0a2;
    --shadow: rgba(60, 45, 20, 0.25);
  }
  * { box-sizing: border-box; margin: 0; padding: 0; }
  html, body {
    width: 1200px; height: 914px; overflow: hidden;
    background: var(--page);
  }
  .canvas {
    width: 1200px; height: 914px;
    display: flex; align-items: center; justify-content: center;
  }
  .business-card {
    width: 1000px; height: 600px;
    background: var(--card-edge);
    padding: 34px;
    box-shadow: 0 18px 40px var(--shadow);
  }
  .card-face {
    position: relative;
    width: 100%; height: 100%;
    background: var(--card-gold);
  }
  .brand {
    position: absolute; left: 400px; top: 70px;
    display: flex; align-items: center; gap: 22px;
  }
  .brand-mark {
    width: 74px; height: 74px;
    border: 4px solid var(--ink-light);
    border-radius: 50%;
  }
  .brand-name {
    font-family: "Montserrat", sans-serif;
    font-weight: 600;
    font-size: 64px;
    letter-spacing: 2px;
    color: var(--ink-light);
  }
  .holder-name {
    position: absolute; left: 300px; top: 262px;
    font-family: "Montserrat", sans-serif;
    font-weight: 600; font-size: 22px;
    color: var(--ink-light);
  }
  .address {
    position: absolute; left: 230px; top: 318px;
    width: 320px; text-align: right;
    font-family: "Cormorant SC", serif;
    font-weight: 500; font-size: 20px; line-height: 1.5;
    color: var(--ink-soft);
    letter-spacing: 0.5px;
  }
  .divider {
    position: absolute; left: 574px; top: 300px;
    width: 2px; height: 190px;
    background: var(--ink-soft);
  }
  .contact-list {
    position: absolute; left: 596px; top: 300px;
    list-style: none;
    font-family: "Cormorant SC", serif;
    font-weight: 500; font-size: 19px;
    color: var(--ink-soft);
  }
  .contact-list li {
    display: flex; align-items: center; gap: 10px;
    height: 38px;
  }
  .contact-icon { width: 20px; height: 20px; flex: none; }
</style>
</head>
<body>
<main class="canvas">
  <section class="business-card" aria-label="R.T. M&amp;P business card">
    <div class="card-face">
      <div class="brand">
        <span class="brand-mark"></span>
        <span class="brand-name">R.T. M&amp;P</span>
      </div>

      <p class="holder-name">Odel Krasniak</p>

      <p class="address">7281 Porravel Blvd. Suite 382<br>Ashgrove Heights, CA 90417</p>

      <span class="divider"></span>

      <ul class="contact-list">
        <li>
          <svg class="contact-icon" viewBox="0 0 20 20"><circle cx="10" cy="10" r="9.5" fill="#f3e0a2"/><path d="M7 5.5l2 2-1.2 1.3a6 6 0 0 0 3.4 3.4L12.5 11l2 2-1.3 1.5C9.5 14.3 5.7 10.5 5.5 6.8z" fill="#cda547"/></svg>
          555-210-4471
        </li>
        <li>
          <svg class="contact-icon" viewBox="0 0 20 20"><circle cx="10" cy="10" r="9.5" fill="#f3e0a2"/><path d="M7 5.5l2 2-1.2 1.3a6 6 0 0 0 3.4 3.4L12.5 11l2 2-1.3 1.5C9.5 14.3 5.7 10.5 5.5 6.8z" fill="#cda547"/></svg>
          555-318-9062
        </li>
        <li>
          <svg class="contact-icon" viewBox="0 0 20 20"><circle cx="10" cy="10" r="9.5" fill="#f3e0a2"/><rect x="6" y="5" width="8" height="10" rx="1.2" fill="#cda547"/></svg>
          555-604-2285
        </li>
        <li>
          <svg class="contact-icon" viewBox="0 0 20 20"><circle cx="10" cy="10" r="9.5" fill="#f3e0a2"/><rect x="5" y="6.5" width="10" height="7" fill="#cda547"/><path d="M5 6.5l5 4 5-4" fill="none" stroke="#f3e0a2" stroke-width="1"/></svg>
          odel@tinmarrowseek.com
        </li>
        <li>
          <svg class="contact-icon" viewBox="0 0 20 20"><circle cx="10" cy="10" r="9.5" fill="#f3e0a2"/><circle cx="10" cy="10" r="5" fill="none" stroke="#cda547" stroke-width="1.4"/><path d="M5 10h10M10 5v10" stroke="#cda547" stroke-width="1.2"/></svg>
          www.tinmarrowseek.com
        </li>
      </ul>
    </div>
  </section>
</main>
</body>
</html>
```